Weihnachtskarten-Design
Zielgruppe
Rechtsanwaltskanzlei
Aufgabenstellung
Es soll eine kreative Weihnachtskarte werden / das corporate Design der Kanzlei sollte beachtet werden (siehe www.kanzlei-drbrammel.de). Die Weihnachtskarte soll 4 Seiten umfassen (also eine aufklappbare Weihnachtskarte).

```html
<!DOCTYPE html>
<html lang="de">
<head>
<meta charset="utf-8">
<title>Weihnachtskarte – Halvern &amp; Partner</title>
<link rel="stylesheet" href="https://fonts.googleapis.com/css2?family=Merriweather:wght@400;900&display=swap">
<style>
  :root {
    --stage: #cbd3e1;
    --navy: #13244a;
    --navy-soft: #1c3060;
    --paper: #ffffff;
    --paper-shade: #eef0f4;
    --ring-light: #e9edf4;
    --ring-dark: #1a2a52;
    --text-font: "Merriweather", Georgia, serif;
  }
  * { box-sizing: border-box; margin: 0; padding: 0; }
  html, body { width: 1200px; height: 800px; overflow: hidden; }
  body {
    background: var(--stage);
    font-family: var(--text-font);
    display: flex;
    align-items: center;
    justify-content: center;
    gap: 40px;
  }
  .page {
    position: relative;
    width: 360px;
    height: 360px;
    overflow: hidden;
  }
  .spread { display: flex; box-shadow: 0 10px 30px rgba(20,36,74,.15); }
  .cover {
    background: radial-gradient(circle at 50% 55%, var(--navy-soft), var(--navy) 70%);
    box-shadow: 0 10px 30px rgba(20,36,74,.15);
  }
  .inside { background: var(--paper); }
  .inside-left { background: linear-gradient(90deg, var(--paper) 80%, var(--paper-shade)); }

  .string {
    position: absolute;
    left: 50%;
    top: 0;
    width: 2px;
    height: 95px;
    transform: translateX(-50%);
  }
  .cover .string { background: var(--paper); }
  .inside .string { background: var(--navy); }

  .ornament {
    position: absolute;
    left: 50%;
    top: 185px;
    width: 190px;
    height: 190px;
    transform: translate(-50%, -50%);
  }
  .ornament-ring {
    position: absolute;
    inset: 0;
    border-radius: 50%;
  }
  .cover .ornament-ring {
    background: radial-gradient(circle, transparent 58%, var(--ring-light) 59%, var(--ring-light) 78%, transparent 80%);
  }
  .inside .ornament-ring {
    background: radial-gradient(circle, transparent 58%, var(--ring-dark) 59%, var(--ring-dark) 78%, transparent 80%);
  }
  .bauble {
    position: absolute;
    left: 50%;
    top: 50%;
    width: 118px;
    height: 118px;
    transform: translate(-50%, -50%);
    border-radius: 50%;
    background: var(--paper);
    border: 5px solid var(--paper);
    box-shadow: inset 0 3px 8px rgba(0,0,0,.18), 0 2px 4px rgba(0,0,0,.15);
    display: flex;
    flex-direction: column;
    align-items: center;
    justify-content: center;
    color: var(--navy);
    text-align: center;
  }
  .greeting-main {
    font-weight: 900;
    font-size: 15px;
    line-height: 1.05;
    letter-spacing: .5px;
  }
  .greeting-main span { display: block; font-size: 11px; }
  .greeting-rule {
    width: 70px;
    border-top: 1px dotted var(--navy);
    margin: 4px 0 3px;
  }
  .greeting-sub { font-size: 8px; font-weight: 400; }

  .firm-name {
    position: absolute;
    left: 0;
    right: 0;
    bottom: 26px;
    text-align: center;
    font-size: 11px;
    font-weight: 400;
    letter-spacing: 2px;
    color: var(--navy);
  }
  .cover .firm-name { color: var(--paper); }
</style>
</head>
<body>

  <section class="page cover">
    <div class="string"></div>
    <div class="ornament">
      <div class="ornament-ring" role="img" aria-label="Kranz aus weißen Schneeflocken rund um die Weihnachtskugel"></div>
      <div class="bauble">
        <p class="greeting-main">MERRY<span>CHRISTMAS</span></p>
        <div class="greeting-rule"></div>
        <p class="greeting-sub">&amp; Happy New Year</p>
      </div>
    </div>
    <p class="firm-name">Halvern &amp; Partner</p>
  </section>

  <section class="spread">
    <div class="page inside inside-left">
      <div class="string"></div>
      <div class="ornament">
        <div class="ornament-ring" role="img" aria-label="Kranz aus dunkelblauen Schneeflocken rund um die Weihnachtskugel"></div>
        <div class="bauble">
          <p class="greeting-main">MERRY<span>CHRISTMAS</span></p>
          <div class="greeting-rule"></div>
          <p class="greeting-sub">&amp; Happy New Year</p>
        </div>
      </div>
      <p class="firm-name">Halvern &amp; Partner</p>
    </div>

    <div class="page inside inside-right">
      <div class="string"></div>
      <div class="ornament">
        <div class="ornament-ring" role="img" aria-label="Kranz aus dunkelblauen Schneeflocken rund um die leere Weihnachtskugel"></div>
        <div class="bauble"></div>
      </div>
      <p class="firm-name">Halvern &amp; Partner</p>
    </div>
  </section>

</body>
</html>
```